Web Design Project - wine stock exchange

This page shall be informative about Cellar Crest Wines to express their values. And, like the normal stock exchanges, clients can bid and ask for price indications.
Also, the clients can generate their own wines like the winemakers provide individual barrowls to design by the clients.

```html
<!DOCTYPE html>
<html lang="en">
<head>
<meta charset="utf-8">
<title>Vintage Bourse – Wine Store</title>
<link rel="stylesheet" href="https://fonts.googleapis.com/css2?family=Libre+Franklin:wght@400;600&family=Noto+Sans:wght@400;700&family=Federo&family=Tinos:wght@400;700&display=swap">
<style>
:root{
  --page-bg:#cccb98;
  --column:#ffffff;
  --wine:#6e0a12;
  --wine-dark:#4a050b;
  --wine-light:#86101b;
  --black:#000000;
  --card:#cccccc;
  --olive:#cccb98;
  --bid:#7a6424;
  --details:#7c1a1e;
  --price:#e0383c;
  --label:#7a3a32;
  --star:#e8303a;
  --cream:#f3eec8;
  --winner-red:#c8353b;
}
*{margin:0;padding:0;box-sizing:border-box}
html,body{width:1200px;height:900px;overflow:hidden}
body{background:var(--page-bg);font-family:"Noto Sans",sans-serif;position:relative}
.column{position:absolute;left:219px;top:0;width:813px;height:900px;background:var(--column)}
.topline{position:absolute;left:230px;top:0;width:792px;height:10px;background:#d4d4d4}
.nav{position:absolute;left:230px;top:10px;width:792px;height:46px;background:linear-gradient(#7a0c15,#520710);border-bottom:2px solid #2a0206;display:flex;justify-content:center;align-items:center}
.nav a{color:#fff;text-decoration:none;font-family:"Libre Franklin",sans-serif;font-size:14px;padding:0 11px}
.nav .star{color:var(--star);font-size:13px;padding:0 2px}
.hero{position:absolute;left:230px;top:57px;width:792px;height:247px;background:linear-gradient(90deg,#1c1c1c 0%,#3a3a3a 35%,#5a3a30 55%,#3a0c0c 75%,#2a0a0a 100%)}
.hero-name{position:absolute;left:292px;top:160px;font-family:"Libre Franklin",sans-serif;font-weight:400;font-size:30px;color:var(--cream)}
.search{position:absolute;left:230px;top:305px;width:792px;height:45px;background:linear-gradient(var(--wine-light),var(--wine-dark));display:flex;align-items:center;padding-left:38px;gap:9px;padding-bottom:6px}
.search label{color:#fff;font-size:10px;font-weight:700}
.search .field{width:121px;height:17px;background:#f0e6e8;border:1px solid #bbb}
.search .btn{height:18px;padding:0 5px;font-size:10px;font-weight:700;background:#dcd8b4;border:2px outset #eee;color:#000;line-height:14px}
.card{position:absolute;top:352px;width:191px;height:272px;background:var(--card)}
.card h3{height:29px;background:var(--black);color:#fff;font-size:10px;font-weight:700;line-height:29px;padding-left:24px}
.card .photo{position:absolute;left:9px;top:40px;width:173px;height:84px;border:3px solid #fff;background:linear-gradient(160deg,#d2d0a0 30%,#2a2a2a 45%,#d8d6c8 65%,#c9c79a 90%)}
.card .price{position:absolute;left:16px;top:134px;font-family:"Tinos",serif;font-size:12px;color:var(--label);font-weight:700;line-height:15px}
.card .price span{color:var(--price);font-weight:400}
.card p{position:absolute;left:16px;top:170px;font-size:9px;line-height:11px;color:#000;width:160px;white-space:nowrap}
.card .bid{position:absolute;left:13px;top:221px;width:79px;height:22px;background:var(--bid);color:#fff;font-size:10px;font-weight:700;line-height:22px;padding-left:13px;border-bottom:2px solid #4a3c12}
.card .details{position:absolute;left:13px;top:249px;width:53px;height:16px;background:var(--details);color:#fff;font-size:10px;font-weight:700;line-height:16px;padding-left:10px}
.pager{position:absolute;left:231px;top:625px;width:791px;height:22px;background:var(--olive);display:flex;justify-content:flex-end;align-items:center;padding-right:12px;gap:9px;font-size:12px}
.pager .all{font-size:10px}
.news{position:absolute;left:231px;top:650px;width:391px;height:205px;background:radial-gradient(circle at 40% 40%,#7c0d16,#4e060c)}
.news h2{position:absolute;left:18px;top:16px;font-family:"Federo",sans-serif;font-weight:400;font-size:24px;color:#fff}
.news p{position:absolute;left:19px;width:222px;font-size:9.5px;line-height:12px;color:#fff}
.news u{text-decoration:underline}
.news .bottles{position:absolute;left:246px;top:5px;width:112px;height:198px;background:linear-gradient(90deg,transparent 0%,#c9b070 15%,#3a1028 55%,#2a0a1a 75%,transparent 100%);opacity:.9}
.winners{position:absolute;left:630px;top:650px;width:392px;height:205px;background:var(--card)}
.winners h2{position:absolute;left:24px;top:15px;font-family:"Federo",sans-serif;font-weight:400;font-size:25px;color:var(--winner-red)}
.winners .quote{position:absolute;left:26px;top:51px;width:347px;height:113px;background:#fff;box-shadow:0 1px 3px rgba(0,0,0,.3)}
.winners .avatar{position:absolute;left:16px;top:18px;width:81px;height:77px;border:6px solid #c8c8c8;background:linear-gradient(#e8e8e8,#b8b8b8)}
.winners .quote p{position:absolute;left:114px;top:17px;width:228px;font-family:"Tinos",serif;font-size:12px;line-height:15px;color:#222}
.winners .more{position:absolute;left:324px;top:175px;font-size:9px;font-weight:700;color:#222}
.footer{position:absolute;left:231px;top:858px;width:791px;height:33px;background:var(--black);color:#ddd;font-size:10px;display:flex;justify-content:center;align-items:center;gap:6px}
.footer .gap{width:6px}
</style>
</head>
<body>
<div class="column"></div>
<div class="topline"></div>
<nav class="nav">
  <a href="#">Home</a><span class="star">★</span>
  <a href="#">Buy Wine</a><span class="star">★</span>
  <a href="#">Sell Wine</a><span class="star">★</span>
  <a href="#">Login</a><span class="star">★</span>
  <a href="#">Blog</a><span class="star">★</span>
  <a href="#">Contact Us</a>
</nav>
<div class="hero" role="img" aria-label="Photo of a glass of red wine beside three red wine bottles"></div>
<h1 class="hero-name">Vintage Bourse</h1>
<form class="search">
  <label>Find Wine :</label>
  <div class="field"></div>
  <div class="btn">Search</div>
</form>

<article class="card" style="left:231px">
  <h3>2002 St Emilion France</h3>
  <div class="photo" role="img" aria-label="Wine bottle lying on its side"></div>
  <div class="price">MRP: <span>699.00/-</span><br>Last Sold: Rs. 0.33</div>
  <p>Fantastically elegant Fantastically<br>elegant with great finesse<br>with great finesse</p>
  <div class="bid">BID NOW</div>
  <div class="details">Details</div>
</article>
<article class="card" style="left:431px">
  <h3>2002 St Emilion France</h3>
  <div class="photo" role="img" aria-label="Dark wine bottle lying on its side"></div>
  <div class="price">MRP: <span>699.00/-</span><br>Last Sold: Rs. 0.33</div>
  <p>Fantastically elegant Fantastically<br>elegant with great finesse<br>with great finesse</p>
  <div class="bid">BID NOW</div>
  <div class="details">Details</div>
</article>
<article class="card" style="left:631px">
  <h3>2002 St Emilion France</h3>
  <div class="photo" role="img" aria-label="Wine bottle lying on its side"></div>
  <div class="price">MRP: <span>699.00/-</span><br>Last Sold: Rs. 0.33</div>
  <p>Fantastically elegant Fantastically<br>elegant with great finesse<br>with great finesse</p>
  <div class="bid">BID NOW</div>
  <div class="details">Details</div>
</article>
<article class="card" style="left:831px">
  <h3>2002 St Emilion France</h3>
  <div class="photo" role="img" aria-label="Red wine bottle lying on its side"></div>
  <div class="price">MRP: <span>699.00/-</span><br>Last Sold: Rs. 0.33</div>
  <p>Fantastically elegant Fantastically<br>elegant with great finesse<br>with great finesse</p>
  <div class="bid">BID NOW</div>
  <div class="details">Details</div>
</article>

<div class="pager"><span>1</span><span>2</span><span>3</span><span>4</span><span class="all">View All &gt;&gt;</span></div>

<section class="news">
  <h2>What's New Here?</h2>
  <p style="top:55px">Online wine auction site Vintage Bourse offers a trading platform to buy and sell rare and vintage fine wines via real-time auctions.</p>
  <p style="top:103px">See our guide on how to sell wine at auction using Vintage Bourse, request a valuation or start <u>buying or selling</u> now.</p>
  <p style="top:151px">To hear the latest news and receive up to the minute information on newly offered wines, why not follow us on Chirper or subscribe to our blog?</p>
  <div class="bottles" role="img" aria-label="Two glasses of sparkling wine beside a bottle"></div>
</section>

<section class="winners">
  <h2>Happy Winners</h2>
  <div class="quote">
    <div class="avatar" role="img" aria-label="Portrait of a winner"></div>
    <p>Corkline Reverse Auction is one of the most incredible concepts conceived in e-commerce and offers an absorbing on-line gaming activity supported by</p>
  </div>
  <div class="more">more &gt;&gt;</div>
</section>

<footer class="footer">© Copyright 2012 Cellar Crest Wines. All Rights Reserved.<span class="gap"></span>Privacy Policy | Terms &amp; Conditions</footer>
</body>
</html>
```